Wochen Speiseplan
Zielgruppe
Hospiz
Aufgabenstellung
Wir brauchen für unser Hospiz einen Wochenspeiseplan. Es soll eine Powerpointseite im A4 Format erstellt werden. Wir brauchen 4 unterschiedliche Seiten - für jede Jahreszeit einen Entwurf. Der Speiseplan soll von uns selbst ausgefüllt werden können.
Inhalte: Montag - Sonntag jeweils Mittag- und Abendessen. (Aufgebaut wie ein Stundenplan.). Möglichst große Schriftgröße. In der Fußnote bitte: "Änderungen vorbehalten schreiben". Das ganze soll professionell, aber dennoch liebevoll gestaltet sein. Es soll unseren Bewohnern "Liust machen" draufzuschauen. Der Plan wird jede Woche neu ausgefüllt, ausgedruckt und laminiert. Sollte also einfach zu handhaben sein.
Das Hospiz lebt von Spenden, daher bitte nicht zu aufwendig, dafür aber bezahlbar machen.

```html
<!DOCTYPE html>
<html lang="de">
<head>
<meta charset="utf-8">
<title>Wochen-Speiseplan Herbst</title>
<link href="https://fonts.googleapis.com/css2?family=Pinyon+Script&family=Arimo:wght@400&display=swap" rel="stylesheet">
<style>
  :root {
    --leaf-dark: #5a1606;
    --leaf-mid: #b5400e;
    --leaf-bright: #f0a035;
    --leaf-light: #fbd58a;
    --title-white: #fffaf0;
    --title-glow: #f28a1c;
    --panel: rgba(255, 255, 255, 0.42);
    --ink: #111111;
  }
  * { margin: 0; padding: 0; box-sizing: border-box; }
  html, body { width: 1200px; height: 849px; overflow: hidden; background: #ffffff; }
  .menu-sheet {
    position: relative;
    width: 1200px;
    height: 849px;
    overflow: hidden;
    font-family: "Arimo", Arial, sans-serif;
    color: var(--ink);
  }
  .autumn-backdrop {
    position: absolute;
    inset: 0;
    background:
      radial-gradient(ellipse 420px 300px at 700px 560px, var(--leaf-light) 0%, transparent 70%),
      radial-gradient(ellipse 360px 260px at 180px 620px, var(--leaf-bright) 0%, transparent 75%),
      radial-gradient(ellipse 300px 220px at 1050px 420px, var(--leaf-bright) 0%, transparent 75%),
      radial-gradient(ellipse 380px 200px at 650px 150px, var(--leaf-mid) 0%, transparent 80%),
      linear-gradient(180deg, var(--leaf-dark) 0%, var(--leaf-mid) 40%, var(--leaf-bright) 75%, var(--leaf-mid) 100%);
  }
  .script {
    font-family: "Pinyon Script", cursive;
    font-weight: 400;
    line-height: 1;
  }
  .title, .greeting {
    position: absolute;
    color: var(--title-white);
    text-shadow: 0 0 4px var(--title-glow), 0 0 10px var(--title-glow), 0 0 18px rgba(242, 138, 28, 0.7);
  }
  .title { left: 300px; top: 40px; font-size: 172px; }
  .greeting { font-size: 96px; }
  .greeting--first { left: 48px; top: 88px; }
  .greeting--second { left: 104px; top: 210px; }
  .plan-panel {
    position: absolute;
    left: 80px; top: 340px;
    width: 1037px; height: 467px;
    background: var(--panel);
  }
  .grid-lines { position: absolute; inset: 0; pointer-events: none; }
  .day {
    position: absolute;
    top: 352px;
    width: 124px;
    text-align: center;
    font-size: 46px;
  }
  .meal-label {
    position: absolute;
    left: 92px;
    width: 160px;
    text-align: center;
    font-size: 42px;
    line-height: 0.95;
  }
  .meal-label--lunch { top: 412px; }
  .meal-label--dinner { top: 648px; }
  .dish {
    position: absolute;
    top: 418px;
    width: 118px;
    font-size: 18px;
    line-height: 1.25;
  }
  .week-range {
    position: absolute;
    left: 82px; top: 811px;
    font-size: 31px;
  }
  .reservation {
    position: absolute;
    right: 8px; top: 826px;
    font-size: 16px;
  }
</style>
</head>
<body>
<main class="menu-sheet">
  <div class="autumn-backdrop" role="img" aria-label="Hintergrundfoto mit Herbstlaub in Rot-, Orange- und Goldtönen"></div>

  <p class="script greeting greeting--first">Guten</p>
  <p class="script greeting greeting--second">Appetit!</p>
  <h1 class="script title">Speiseplan</h1>

  <section class="plan-panel" aria-label="Wochenplan"></section>

  <svg class="grid-lines" width="1200" height="849" viewBox="0 0 1200 849" aria-hidden="true">
    <g stroke="#000" stroke-width="4" stroke-dasharray="6 8" stroke-linecap="round">
      <line x1="260" y1="358" x2="260" y2="786"/>
      <line x1="383" y1="358" x2="383" y2="786"/>
      <line x1="508" y1="358" x2="508" y2="786"/>
      <line x1="635" y1="358" x2="635" y2="786"/>
      <line x1="760" y1="358" x2="760" y2="786"/>
      <line x1="888" y1="358" x2="888" y2="786"/>
      <line x1="1012" y1="358" x2="1012" y2="786"/>
      <line x1="110" y1="572" x2="1085" y2="572" stroke-dasharray="10 8"/>
    </g>
  </svg>

  <span class="script day" style="left:262px">Mo</span>
  <span class="script day" style="left:385px">Di</span>
  <span class="script day" style="left:510px">Mi</span>
  <span class="script day" style="left:637px">Do</span>
  <span class="script day" style="left:762px">Fr</span>
  <span class="script day" style="left:890px">Sa</span>
  <span class="script day" style="left:1014px">So</span>

  <span class="script meal-label meal-label--lunch">Mittag-<br>Essen</span>
  <span class="script meal-label meal-label--dinner">Abend-<br>Essen</span>

  <p class="dish" style="left:276px">Spargel-<br>suppe<br>&amp; Dessert</p>
  <p class="dish" style="left:391px">Schweine-<br>medallions<br>in Champig-<br>non-Sahne-<br>Soße mit<br>Kroketten</p>
  <p class="dish" style="left:524px">Rindergu-<br>lasch mit<br>Nudeln<br>dazu Salat</p>
  <p class="dish" style="left:649px">Schnitzel<br>Wiener Art<br>mit div.<br>Beilagen<br>dazu Salat</p>
  <p class="dish" style="left:779px">Tomaten-<br>crem-<br>suppe<br>dazu<br>Ciabatta</p>

  <p class="week-range">Woche vom 07.04.2014 bis 13.04.2014</p>
  <p class="reservation">*Änderungen vorbehalten*</p>
</main>
</body>
</html>
```